New Update: I am changing the title of the book and the back cover text. Title was too long before. Same style as before.
New Title: Under the Quiet Sky
New Subtitle: A Gardener’s Notes on Patience (italics on front cover)

Back cover text:
Under the Quiet Sky: A Gardener’s Notes on Patience offers clear, compassionate guidance for those recovering from total loss. Drawing from his experience as a Brennick Flood survivor, Tobias Quellhorst shares practical advice on insurance, rebuilding, and emotional healing, along with lessons in strength and community. This is not a book about tragedy; it’s about perseverance and renewal. Under the Quiet Sky is a trusted companion for anyone rebuilding life, home, and hope after disaster.

Font styles to use
Serif

Colors
EB3D1F
EC4F4E
F09395
F8D3D4
FCEDEE

Requirements
Should not have
• No pictures or anything related to fire on the cover.

```html
<!DOCTYPE html>
<html lang="en">
<head>
<meta charset="utf-8">
<title>Under the Quiet Sky – Book Cover Wrap</title>
<link rel="stylesheet" href="https://fonts.googleapis.com/css2?family=Abril+Fatface&family=Montserrat:wght@600&family=Playfair+Display:ital,wght@0,700;0,900;1,900&display=swap">
<style>
  :root {
    --ink-white: #ffffff;
    --bg-dark: #1e0e0c;
    --bg-mid: #4a1c15;
    --bg-warm: #8c3f2b;
    --bg-glow: #a9573c;
    --photo-light: #d9d2c6;
    --photo-dark: #2a2a30;
    --panel-white: #ffffff;
  }
  * { margin: 0; padding: 0; box-sizing: border-box; }
  html, body { width: 1200px; height: 865px; overflow: hidden; background: var(--bg-dark); }
  .wrap {
    position: relative;
    width: 1200px; height: 865px;
    overflow: hidden;
    color: var(--ink-white);
    background:
      radial-gradient(ellipse 420px 520px at 930px 560px, var(--bg-glow) 0%, rgba(169,87,60,0) 75%),
      linear-gradient(160deg, var(--bg-dark) 0%, var(--bg-mid) 45%, var(--bg-warm) 100%);
  }

  /* Back cover */
  .back-title {
    position: absolute; left: 104px; top: 128px; width: 382px; text-align: center;
    font-family: "Playfair Display", serif; font-weight: 900;
    font-size: 14px; text-transform: uppercase;
    white-space: nowrap;
  }
  .back-copy {
    position: absolute; left: 104px; top: 167px; width: 382px;
    font-family: "Montserrat", sans-serif; font-weight: 600;
    font-size: 13.6px; line-height: 17.2px; letter-spacing: 0.7px;
    text-transform: uppercase;
  }
  .back-copy p + p { margin-top: 17.2px; }
  .back-rule {
    position: absolute; left: 192px; top: 559px; width: 196px; height: 3px;
    background: var(--ink-white);
  }
  .author-photo {
    position: absolute; left: 105px; top: 581px; width: 120px; height: 123px;
    border: 2px solid var(--ink-white);
    background: linear-gradient(180deg, var(--photo-light) 0%, var(--photo-light) 55%, var(--photo-dark) 100%);
  }
  .author-caption {
    position: absolute; left: 66px; top: 713px; width: 200px; text-align: center;
    font-family: "Playfair Display", serif; font-weight: 900; font-size: 13px;
    text-transform: uppercase; white-space: nowrap;
  }
  .back-panel {
    position: absolute; left: 344px; top: 718px; width: 165px; height: 88px;
    background: var(--panel-white);
  }

  /* Spine */
  .spine-text {
    position: absolute; left: 591px;
    writing-mode: vertical-rl;
    font-family: "Playfair Display", serif; font-weight: 900;
    font-size: 12px; text-transform: uppercase; white-space: nowrap;
  }
  .spine-title { top: 153px; }
  .spine-author { top: 556px; }

  /* Front cover */
  .front { position: absolute; left: 640px; top: 0; width: 535px; text-align: center; }
  .front-title {
    position: absolute; left: 0; top: 78px; width: 100%;
    font-family: "Abril Fatface", serif; font-weight: 400;
    font-size: 100px; line-height: 102px; text-transform: uppercase;
    text-shadow: 2px 3px 6px rgba(0,0,0,0.35);
  }
  .front-subtitle {
    position: absolute; left: 0; top: 508px; width: 100%;
    font-family: "Playfair Display", serif; font-weight: 900; font-style: italic;
    font-size: 25px; text-transform: uppercase; white-space: nowrap;
    text-shadow: 1px 2px 4px rgba(0,0,0,0.3);
  }
  .front-tagline {
    position: absolute; left: 0; top: 556px; width: 100%;
    font-family: "Playfair Display", serif; font-weight: 900;
    font-size: 24px; line-height: 33px; text-transform: uppercase;
    text-shadow: 1px 2px 4px rgba(0,0,0,0.3);
  }
  .front-tagline .small { font-size: 16px; }
  .front-author {
    position: absolute; left: 0; top: 752px; width: 100%;
    font-family: "Playfair Display", serif; font-weight: 900;
    font-size: 37px; text-transform: uppercase; white-space: nowrap;
    text-shadow: 1px 2px 4px rgba(0,0,0,0.3);
  }
</style>
</head>
<body>
<main class="wrap">
  <section class="back-cover">
    <h2 class="back-title">Under the Quiet Sky: A Gardener’s Notes on Patience</h2>
    <div class="back-copy">
      <p>Under the Quiet Sky: A Gardener’s Notes on Patience offers clear, compassionate guidance for those recovering from total loss. Drawing from his experience as a Brennick Flood survivor, Tobias Quellhorst shares practical advice on insurance, rebuilding, and emotional healing, along with lessons in strength and community.</p>
      <p>This is not a book about tragedy; it’s about perseverance and renewal.</p>
      <p>Under the Quiet Sky is a trusted companion for anyone rebuilding life, home, and hope after disaster.</p>
    </div>
    <div class="back-rule"></div>
    <div class="author-photo" role="img" aria-label="Author portrait photograph"></div>
    <p class="author-caption">Tobias Quellhorst</p>
    <div class="back-panel"></div>
  </section>

  <section class="spine">
    <p class="spine-text spine-title">Under the Quiet Sky: A Gardener’s Notes on Patience</p>
    <p class="spine-text spine-author">Tobias Quellhorst</p>
  </section>

  <section class="front">
    <h1 class="front-title">Under<br>The<br>Quiet<br>Sky</h1>
    <p class="front-subtitle">A Gardener’s Notes on Patience</p>
    <p class="front-tagline">A Journey Through Loss,<br>Recovery, <span class="small">and</span> Rebuilding</p>
    <p class="front-author">Tobias Quellhorst</p>
  </section>
</main>
</body>
</html>
```